WWW.VELTRONA.IT BUSINNES CARD

WE NEED A BUSINESS CARD . I HAVE A COMPANY IN ITALY NR 1 IN HAIR MEDICAL CARE AN HAIR REPLECEMENT . IN CARD I NEED WRITE WEB ADDRESS, MAIL , ADDRESS, TELEPHONE NUMBER , AND NAME
IN THE BACK SIDE I NEED MY DOCTOR LOGO .
MY WEB SITE IS WWW.VELTRONA.IT
Updates

Target Market(s)

CONSUMER B2C

Industry/Entity Type

Hair And Beauty

Contact Information for Business Card

I WANT A MEDICAL BUSINESS CARD.

Font styles to use
Other font styles liked:
• VERDANA

Colors
33a6d7
3176b5
85abd2
aedbee
eaf1f7
ffffff

Requirements
Must have
• I NEED MY LOGO AND LOGO OF DR VELTRONA

```html
<!DOCTYPE html>
<html lang="it">
<head>
<meta charset="utf-8">
<title>Veltrona – Business Card</title>
<link href="https://fonts.googleapis.com/css2?family=Lato:wght@400;700&display=swap" rel="stylesheet">
<style>
  :root {
    --backdrop: #2f2926;
    --card-dark: #0c0c0d;
    --card-light: #ffffff;
    --brand-blue: #3176b5;
    --brand-cyan: #33a6d7;
    --pale-blue: #aedbee;
    --text-light: #e6e6e6;
    --divider: #2a2a2c;
    --mascot-brown: #7a4a2a;
    --mascot-peach: #f2a37e;
  }
  * { margin: 0; padding: 0; box-sizing: border-box; }
  html, body { width: 1200px; height: 844px; overflow: hidden; }
  body {
    background: var(--backdrop);
    font-family: "Lato", Verdana, sans-serif;
    position: relative;
  }
  .card {
    position: absolute;
    top: 272px;
    width: 520px;
    height: 300px;
    box-shadow: 0 10px 30px rgba(0,0,0,.45);
  }
  .card--front { left: 60px; background: var(--card-dark); display: flex; }
  .card--back { left: 620px; background: var(--card-light); }

  .brand-side {
    width: 54%;
    display: flex;
    flex-direction: column;
    justify-content: center;
    padding-left: 40px;
  }
  .brand-name {
    display: flex;
    align-items: center;
    gap: 10px;
    font-size: 34px;
    font-weight: 700;
    color: var(--brand-blue);
  }
  .brand-dot {
    width: 22px; height: 22px; border-radius: 50%;
    background: var(--brand-cyan);
  }
  .brand-tagline {
    margin-top: 6px;
    font-size: 10.5px;
    letter-spacing: .5px;
    color: var(--brand-cyan);
    text-transform: uppercase;
  }

  .contact-side {
    width: 46%;
    border-left: 1px solid var(--divider);
    padding: 56px 0 0 26px;
    color: var(--text-light);
    font-size: 15px;
    line-height: 1.3;
  }
  .person-name { font-size: 19px; font-weight: 700; color: var(--brand-blue); }
  .person-name span { color: var(--brand-cyan); }
  .person-role { margin-bottom: 10px; }
  .contact-line { display: flex; align-items: center; gap: 8px; }
  .contact-line svg { width: 12px; height: 12px; fill: var(--brand-cyan); flex: none; }
  .address { margin-top: 12px; }

  .mascot {
    position: absolute;
    left: 210px; top: 30px;
    width: 90px; height: 220px;
    border-radius: 45px 45px 40px 40px;
    background: linear-gradient(180deg, var(--mascot-brown) 0%, #9a6a44 60%, var(--mascot-peach) 100%);
  }
  .doctor-name {
    position: absolute;
    left: 292px; top: 120px;
    transform: rotate(90deg);
    transform-origin: left top;
    font-size: 16px;
    font-weight: 700;
    color: var(--brand-blue);
    white-space: nowrap;
  }
</style>
</head>
<body>
  <section class="card card--front">
    <div class="brand-side">
      <div class="brand-name"><span class="brand-dot"></span>Veltrona</div>
      <div class="brand-tagline">Cura e reintegrazione dei capelli</div>
    </div>
    <div class="contact-side">
      <div class="person-name">Marco <span>Bellandi</span></div>
      <div class="person-role">Managing Director</div>
      <div class="contact-line">
        <svg viewBox="0 0 24 24"><path d="M6.6 10.8a15 15 0 0 0 6.6 6.6l2.2-2.2c.3-.3.7-.4 1-.2 1.1.4 2.3.6 3.6.6.6 0 1 .4 1 1V20c0 .6-.4 1-1 1A17 17 0 0 1 3 4c0-.6.4-1 1-1h3.5c.6 0 1 .4 1 1 0 1.3.2 2.5.6 3.6.1.3 0 .7-.2 1z"/></svg>
        044-987 210 365
      </div>
      <div class="contact-line">
        <svg viewBox="0 0 24 24"><path d="M2 5h20v14H2z M2 5l10 8 10-8" stroke="#0c0c0d" stroke-width="1.5"/></svg>
        info@veltrona.it
      </div>
      <div class="contact-line">
        <svg viewBox="0 0 24 24"><circle cx="12" cy="12" r="10"/></svg>
        www.veltrona.it
      </div>
      <div class="address">18, Via dei Tigli,<br>Milano, 20121</div>
    </div>
  </section>

  <section class="card card--back">
    <div class="mascot" role="img" aria-label="Doctor mascot illustration"></div>
    <div class="doctor-name">dr. Veltrona</div>
  </section>
</body>
</html>
```